New Company Business Card Design

I have a new company logo and I want a new business card design. I dont know if the logo file i attached is in the correct format or quality. We are a New York City Specialty construction Firm specializing in high risk out of the box projects. I want a simple and classy business card that people will his card is as crisp as the work his company does.

Target Market(s)

Clients in the heavy construction industry in New York City

Industry/Entity Type

Construction Company

Contact Information for Business Card

Simple Classy - DIFFERENT

Font styles to use
Other font styles liked:
• Mach the logo font in some way

Colors

Designer to choose colors to be used in the design.

Requirements
Must have
• Uniqueness
Nice to have
• Nothing particular - Just different and classy - Timeless
Should not have
• Goofy Shit or Gimmicky shit

```html
<!DOCTYPE html>
<html lang="en">
<head>
<meta charset="utf-8">
<title>Halvard Associates – Business Card</title>
<link rel="stylesheet" href="https://fonts.googleapis.com/css2?family=Roboto:wght@400;500;700;900&display=swap">
<style>
  :root {
    --backdrop: #3b3b3d;
    --card-black: #1c1c1e;
    --card-white: #ffffff;
    --brand-blue: #0b5aa6;
    --deep-blue: #0a3f86;
    --ink: #1d1d1f;
    --muted: #555a60;
    --emboss: #5b5b5f;
    --ghost: #efeff0;
  }
  * { box-sizing: border-box; margin: 0; padding: 0; }
  html, body { width: 1200px; height: 1000px; overflow: hidden; }
  body {
    background: var(--backdrop);
    font-family: "Roboto", Arial, sans-serif;
    position: relative;
  }
  .card {
    position: absolute;
    width: 700px;
    height: 400px;
    border-radius: 22px;
    overflow: hidden;
  }
  /* Front: black card */
  .card-front {
    left: 250px; top: 60px;
    background: var(--card-black);
    display: flex; align-items: center; justify-content: center;
  }
  .front-mark {
    display: flex; align-items: center; gap: 18px;
    color: var(--emboss);
    font-weight: 900;
  }
  .front-mark .mark-square {
    width: 46px; height: 46px; background: var(--emboss);
  }
  .front-mark .mark-name {
    font-size: 44px; letter-spacing: 2px; text-transform: uppercase; line-height: 1.05;
  }
  /* Back: white card */
  .card-back {
    left: 250px; top: 530px;
    background: var(--card-white);
  }
  .crane-art {
    position: absolute; right: 60px; top: 30px;
    width: 250px; height: 330px;
    background: linear-gradient(160deg, var(--ghost), #f6f6f7);
  }
  .brand {
    position: absolute; left: 40px; top: 34px;
    display: flex; align-items: center; gap: 12px;
    color: var(--brand-blue); font-weight: 900;
    font-size: 30px; letter-spacing: 1px; text-transform: uppercase;
  }
  .brand .brand-square { width: 28px; height: 28px; background: var(--brand-blue); }
  .person { position: absolute; left: 40px; top: 96px; }
  .person-name { color: var(--brand-blue); font-weight: 500; font-size: 24px; letter-spacing: .5px; }
  .person-title { color: var(--muted); font-size: 14px; margin-top: 2px; }
  .contact { position: absolute; left: 40px; top: 160px; color: var(--ink); font-size: 15px; font-weight: 500; }
  .contact-row { display: flex; align-items: flex-start; gap: 10px; line-height: 20px; }
  .contact-row + .contact-row { margin-top: 4px; }
  .contact-row.address { margin-bottom: 16px; }
  .contact-row svg { width: 13px; height: 13px; margin-top: 3px; flex: none; fill: var(--brand-blue); }
  .footer-black {
    position: absolute; left: 0; bottom: 0; width: 420px; height: 16px; background: #000;
  }
  .footer-blue {
    position: absolute; right: 0; bottom: 0; width: 330px; height: 56px;
    background: var(--deep-blue);
    clip-path: polygon(40px 0, 100% 0, 100% 100%, 0 100%);
    color: #fff; font-size: 17px; font-weight: 500;
    display: flex; align-items: center; justify-content: center; padding-left: 30px;
  }
</style>
</head>
<body>
  <section class="card card-front">
    <div class="front-mark">
      <span class="mark-square"></span>
      <span class="mark-name">Halvard<br>Associates, Inc.</span>
    </div>
  </section>

  <section class="card card-back">
    <div class="crane-art" role="img" aria-label="Faint outline of a lattice construction crane boom"></div>

    <div class="brand">
      <span class="brand-square"></span>
      <span>Halvard Associates, Inc.</span>
    </div>

    <div class="person">
      <p class="person-name">DANIEL REYES</p>
      <p class="person-title">Operations Manager</p>
    </div>

    <div class="contact">
      <div class="contact-row address">
        <svg viewBox="0 0 12 12"><path d="M6 0a4 4 0 0 0-4 4c0 3 4 8 4 8s4-5 4-8a4 4 0 0 0-4-4zm0 5.6A1.6 1.6 0 1 1 6 2.4a1.6 1.6 0 0 1 0 3.2z"/></svg>
        <span>58 Harbor Lane<br>Millbrook, CA 2047</span>
      </div>
      <div class="contact-row">
        <svg viewBox="0 0 12 12"><path d="M2.5 0.5l2 2.3-1 1.4c.7 1.6 2 2.9 3.5 3.6l1.4-1 2.3 2-1 2.2C4.5 10.8 1 7.3.3 2.4z"/></svg>
        <span>+1 (555) 210 4836</span>
      </div>
      <div class="contact-row">
        <svg viewBox="0 0 12 12"><path d="M3 0h6a1 1 0 0 1 1 1v10a1 1 0 0 1-1 1H3a1 1 0 0 1-1-1V1a1 1 0 0 1 1-1zm0 1.5v8h6v-8z"/></svg>
        <span>+1 (555) 210 4837</span>
      </div>
      <div class="contact-row">
        <svg viewBox="0 0 12 12"><path d="M0 2h12v8H0zm1 1v.4l5 3 5-3V3z"/></svg>
        <span>daniel@halvardassoc.com</span>
      </div>
    </div>

    <div class="footer-black"></div>
    <div class="footer-blue">www.halvardassoc.com</div>
  </section>
</body>
</html>
```